Original and striking logo and label design for a young handcrafted dry gin

I am starting a small artisan distillery venture to produce gin. The brand will be called Velmaris which means sunset. As my product is going to be new, modest and small-scale, but at the same time of high quality, I need to differentiate it through its packaging. As within my possibilities I have to resort to standard bottles on the market, it is important to have an original and different label. I want to be able to mark the premium character but at the same time handmade, between vintage or minimalist style (I have not decided yet which would be better). In the annex there is an "Inspiration.rar" file with images of other inspiring gin brands, which are a good example of the sense of excellence that the project must convey. I have already made some label models myself, but I am not satisfied, which I attach. Additionally, I enclose two models of bottles that interest me, with which the label should be able to adapt to both models. Please, if you are not at least at the level of the inspiration images, do not try to propose your model.

Target Market(s)

The product is mainly aimed at young people who appreciate high-quality beverages and who value an artisanal and sustainable product.

Logo Text

Velmaris

Font styles to use
Serif
Decorative
Script

Requirements
Must have
• Reference to the Portuguese sunset (at sea). Reference to what is handcrafted; Portuguese. They must include the following slogan: "Distilled in the glow of the
Portuguese Sunset". The label should allow the following information to be completed by hand: Date distilled; Distiller; Bottle No.; Batch No.

```html
<!DOCTYPE html>
<html lang="en">
<head>
<meta charset="utf-8">
<title>Velmaris Dry Gin Nº 1 — Label</title>
<link rel="stylesheet" href="https://fonts.googleapis.com/css2?family=Josefin+Sans:wght@300;400;600;700&family=Great+Vibes&family=Mrs+Saint+Delafield&family=Courier+Prime:wght@400;700&family=Old+Standard+TT:wght@400;700&display=swap">
<style>
  :root {
    --paper: #ffffff;
    --label-core: #d9532f;
    --label-edge: #c8432a;
    --label-rim: #e5813d;
    --ink-dark: #7a1616;
    --ink-mid: #8d2a1a;
    --cream: #ecbf94;
    --band-top: #ec4e3c;
    --band-bottom: #f3804a;
    --pattern: #e0703e;
    --planet: #a5402c;
  }
  html, body {
    margin: 0;
    width: 1200px;
    height: 1200px;
    overflow: hidden;
    background: var(--paper);
  }
  .canvas { display: block; width: 1200px; height: 1200px; }
  .arc-slogan {
    font-family: "Josefin Sans", sans-serif;
    font-weight: 700;
    font-size: 36px;
    letter-spacing: 4px;
    fill: var(--ink-dark);
  }
  .arc-footer {
    font-family: "Josefin Sans", sans-serif;
    font-weight: 600;
    font-size: 22px;
    letter-spacing: 10px;
    fill: var(--ink-dark);
  }
  .motto-script {
    font-family: "Great Vibes", cursive;
    font-size: 36px;
    fill: var(--ink-dark);
  }
  .brand-name {
    font-family: "Josefin Sans", sans-serif;
    font-weight: 700;
    font-size: 118px;
    letter-spacing: 14px;
    fill: var(--cream);
  }
  .product-line {
    font-family: "Josefin Sans", sans-serif;
    font-weight: 600;
    font-size: 60px;
    letter-spacing: 6px;
    fill: var(--ink-dark);
  }
  .recipe-copy {
    font-family: "Josefin Sans", sans-serif;
    font-weight: 400;
    font-size: 21px;
    letter-spacing: 3px;
    fill: var(--ink-mid);
  }
  .band-motto {
    font-family: "Old Standard TT", serif;
    font-size: 22px;
    fill: var(--ink-dark);
  }
  .band-field {
    font-family: "Courier Prime", monospace;
    font-weight: 700;
    font-size: 15px;
    letter-spacing: 3px;
    fill: var(--ink-dark);
  }
  .band-hand {
    font-family: "Mrs Saint Delafield", cursive;
    font-size: 30px;
    fill: var(--ink-dark);
  }
  .band-entry {
    font-family: "Courier Prime", monospace;
    font-size: 22px;
    letter-spacing: 2px;
    fill: var(--ink-dark);
  }
  .band-serif {
    font-family: "Old Standard TT", serif;
    fill: var(--ink-dark);
  }
  .rule-dotted {
    stroke: var(--ink-dark);
    stroke-width: 1.5;
    stroke-dasharray: 4 3;
  }
</style>
</head>
<body>
<svg class="canvas" viewBox="0 0 1200 1200" xmlns="http://www.w3.org/2000/svg">
  <defs>
    <radialGradient id="label-fill" cx="50%" cy="45%" r="55%">
      <stop offset="0%" stop-color="#dd5a33"/>
      <stop offset="100%" stop-color="#c9442b"/>
    </radialGradient>
    <radialGradient id="pattern-fill" cx="50%" cy="50%" r="50%">
      <stop offset="0%" stop-color="#e2733f" stop-opacity="0.75"/>
      <stop offset="100%" stop-color="#d65a33" stop-opacity="0.2"/>
    </radialGradient>
    <linearGradient id="band-fill" x1="0" y1="0" x2="0" y2="1">
      <stop offset="0%" stop-color="#ec4e3c"/>
      <stop offset="100%" stop-color="#f3804a"/>
    </linearGradient>
    <path id="slogan-arc" d="M238,567 A375 375 0 1 1 962,567"/>
    <path id="footer-arc" d="M266.6,662.5 A385 385 0 0 0 933.4,662.5"/>
  </defs>

  <!-- Round front label -->
  <g class="front-label">
    <circle cx="600" cy="470" r="428" fill="#e5813d"/>
    <circle cx="600" cy="470" r="418" fill="url(#label-fill)"/>

    <circle class="compass-chart" cx="600" cy="470" r="340" fill="url(#pattern-fill)"
            role="img" aria-label="Faint engraved compass rose and nautical chart lines"/>

    <ellipse class="planet-engraving" cx="640" cy="480" rx="240" ry="78"
             transform="rotate(-52 640 480)" fill="#a5402c" fill-opacity="0.35"
             role="img" aria-label="Engraved globe with orbiting ring"/>

    <text class="arc-slogan">
      <textPath href="#slogan-arc" startOffset="50%" text-anchor="middle">DISTILLED IN THE GLOW OF THE PORTUGUESE SUNSET</textPath>
    </text>

    <text class="motto-script" x="600" y="205" text-anchor="middle">A solis ortu</text>
    <text class="motto-script" x="600" y="245" text-anchor="middle">usque ad velmaris</text>

    <text class="brand-name" x="607" y="520" text-anchor="middle">VELMARIS</text>

    <text class="product-line" x="600" y="610" text-anchor="middle">DRY GIN Nº 1</text>

    <text class="recipe-copy" x="600" y="660" text-anchor="middle">PERFECT RECIPE OF</text>
    <text class="recipe-copy" x="600" y="690" text-anchor="middle">10 BOTANICALS BETTWEEN</text>
    <text class="recipe-copy" x="600" y="720" text-anchor="middle">TRADITIONAL AND</text>
    <text class="recipe-copy" x="600" y="750" text-anchor="middle">AUTOCHTHONOUS</text>

    <rect class="alchemist-engraving" x="580" y="764" width="40" height="58" rx="6"
          fill="#9a3220" fill-opacity="0.55"
          role="img" aria-label="Small engraving of a robed alchemist holding a flask"/>

    <text class="arc-footer">
      <textPath href="#footer-arc" startOffset="50%" text-anchor="middle">HANDCRAFTED TUGA PREMIUM GIN</textPath>
    </text>
  </g>

  <!-- Rectangular back band label -->
  <g class="band-label">
    <rect x="90" y="935" width="1020" height="235" fill="url(#band-fill)"/>
    <rect x="104" y="949" width="992" height="207" fill="none" stroke="#c23a2a" stroke-width="2"/>

    <text class="band-motto" x="600" y="990" text-anchor="middle">A solis ortu usque ad velmaris</text>

    <text class="band-field" x="155" y="1020">Master Distiller</text>
    <text class="band-hand" x="290" y="1048">Tomás Ribeiro</text>
    <line class="rule-dotted" x1="155" y1="1052" x2="460" y2="1052"/>

    <text class="band-field" x="150" y="1090">Date distilled</text>
    <text class="band-entry" x="338" y="1090">17/08/20</text>
    <line class="rule-dotted" x1="150" y1="1097" x2="470" y2="1097"/>

    <text class="band-serif" x="148" y="1128" font-size="18">Vol</text>
    <text class="band-serif" x="148" y="1146" font-size="18">Alc</text>
    <text class="band-serif" x="185" y="1146" font-size="34">43%</text>

    <circle class="armillary-engraving" cx="600" cy="1055" r="32" fill="#c23a2a" fill-opacity="0.45"
            role="img" aria-label="Small engraved armillary sphere"/>
    <text class="band-serif" x="600" y="1142" font-size="22" text-anchor="middle">Product of Portugal</text>

    <text class="band-field" x="770" y="1020">Bottle No</text>
    <text class="band-entry" x="900" y="1022">1073</text>
    <line class="rule-dotted" x1="770" y1="1040" x2="1040" y2="1040"/>

    <text class="band-field" x="770" y="1080">Batch No</text>
    <text class="band-entry" x="900" y="1082" font-style="italic">003</text>
    <line class="rule-dotted" x1="770" y1="1097" x2="1040" y2="1097"/>

    <text class="band-serif" x="1040" y="1146" font-size="34" text-anchor="end">70 <tspan font-size="24">cl</tspan></text>
  </g>
</svg>
</body>
</html>
```